Job Coaching - Moval; engaging people to improve their work experience

I need a flyer for Job Coaching. It serves to engage customers (not businesses) with problems in their daily job, typical questions that are handled are:
Do I fit for the job?
Am I using my talents at best in this job?
I have a conflict with my manager/colleagues, what should I do?
My work-life balance is a mess, how can I improve this?
What job fits best with my talents?
I'm getting stressed out from my job, what can I do?
....
This Flyer will be available at GP's, therpeutic practices, pharamcists,...
this flyer should put people in action to contact me
Flyer can be created in English, in the final one the text should be in Dutch; I will make the translation of the selected flyer and provide it at the end

Target Market(s)

consumers / customers / people having a job, but somewhat stuck in it

Industry/Entity Type

Professional Coaching

Requirements
Must have
• the questions mentioned in the project description; mobile number: 0472/318946; email: tom.verlinde@movalcoaching.example; website: www.movalcoaching.example ; it should make also reference to 'Career guidance cheques of the GBRO'

```html
<!DOCTYPE html>
<html lang="en">
<head>
<meta charset="utf-8">
<title>Moval – Career Counseling</title>
<link href="https://fonts.googleapis.com/css2?family=Roboto:wght@400;500;700&display=swap" rel="stylesheet">
<style>
  :root{
    --teal:#35a99e;
    --teal-deep:#2a978c;
    --slate:#5f5f62;
    --ink:#2e2e30;
    --mist:#ececee;
    --mist-light:#f7f7f8;
    --night:#262626;
    --white:#ffffff;
  }
  *{box-sizing:border-box;margin:0;padding:0}
  html,body{width:833px;height:1200px;overflow:hidden;background:#e6e6e6}
  body{font-family:"Roboto",Arial,sans-serif;color:var(--ink)}
  .flyer{
    position:relative;width:833px;height:1200px;overflow:hidden;
    background:linear-gradient(to bottom,var(--mist) 420px,var(--mist-light) 600px,var(--mist-light) 740px,#e9e9eb 830px,var(--mist) 1070px);
  }
  .header-art{position:absolute;left:0;top:0}
  .brand{position:absolute;left:433px;top:72px;display:flex;align-items:center;gap:14px}
  .brand-dot{width:112px;height:112px;border-radius:50%;background:var(--slate)}
  .brand-name{font-size:70px;font-weight:700;color:var(--teal);line-height:1;letter-spacing:1px}
  .brand-tagline{position:absolute;left:560px;top:155px;font-size:19px;color:var(--slate);font-weight:500}
  .title{position:absolute;left:446px;font-weight:700;font-size:46px;letter-spacing:3px;line-height:1}
  .title-career{top:212px;color:var(--slate)}
  .title-counseling{top:268px;color:var(--teal)}
  .intro{position:absolute;left:0;width:833px;top:383px;text-align:center;line-height:35px;font-size:26px}
  .intro-lead{color:var(--teal);font-weight:700}
  .intro-sub{color:var(--ink);font-weight:400}
  .question{position:absolute;display:flex;align-items:center;gap:21px}
  .question svg{flex:none}
  .question p{color:var(--teal);font-weight:500;font-size:15.5px;line-height:20.5px}
  .story{position:absolute;left:72px;top:680px;font-size:13px;letter-spacing:.8px;line-height:16.8px;color:var(--ink)}
  .story p{margin-bottom:16.5px;position:relative}
  .story .tick{position:absolute;left:-46px;top:2px}
  .w1{width:585px}.w4{width:515px}.w5{width:520px}.w6{width:360px}
  .coach-photo{position:absolute;left:574px;top:706px;width:248px;height:364px;border-radius:120px 120px 0 0;
    background:linear-gradient(160deg,#d9dcdc 0%,#9c3348 45%,#8a2a3c 70%,#2f9d93 100%)}
  .coach-glow{position:absolute;left:640px;top:860px;width:193px;height:210px;
    background:linear-gradient(135deg,rgba(53,169,158,0) 0%,rgba(53,169,158,.6) 60%,var(--teal) 100%)}
  .footer{position:absolute;left:0;top:1070px;width:833px;height:130px;background:var(--night)}
  .ribbon{position:absolute;left:0;top:1048px;width:473px;height:43px;background:var(--teal);
    border:2px solid #e9f4f2;border-left:none;border-radius:0 22px 22px 0;
    box-shadow:0 6px 12px rgba(0,0,0,.45);color:var(--white);font-weight:500;font-size:20px;
    line-height:39px;padding-left:68px}
  .contacts{position:absolute;left:60px;right:44px;top:1118px;display:flex;justify-content:space-between;align-items:center;color:var(--white)}
  .contact{display:flex;align-items:center;gap:9px;font-weight:500;font-size:13px;letter-spacing:.6px}
  .contact-phone{font-size:19px;letter-spacing:1.2px;font-weight:700}
</style>
</head>
<body>
<div class="flyer">

  <svg class="header-art" width="833" height="420" viewBox="0 0 833 420">
    <defs>
      <linearGradient id="photoTone" x1="0" y1="0" x2="1" y2="1">
        <stop offset="0" stop-color="#d8d8d8"/>
        <stop offset=".45" stop-color="#7d7d7d"/>
        <stop offset=".75" stop-color="#2d2d2d"/>
        <stop offset="1" stop-color="#9fd3cd"/>
      </linearGradient>
    </defs>
    <path d="M0,0H833V31C500,42 200,60 0,98Z" fill="var(--teal)"/>
    <path d="M0,98C200,60 500,42 833,31V330C700,335 550,352 376,376C250,385 100,395 0,404Z" fill="var(--white)"/>
    <path d="M376,376C550,352 700,335 833,330V357C700,358 550,364 376,377Z" fill="var(--slate)"/>
    <path role="img" aria-label="Photo of a stressed man holding his forehead"
      d="M0,300C60,220 150,150 330,43L376,60V376C250,385 100,395 0,404Z" fill="url(#photoTone)"/>
  </svg>

  <div class="brand">
    <span class="brand-dot"></span>
    <span class="brand-name">Moval</span>
  </div>
  <div class="brand-tagline">professional coaching</div>

  <h1 class="title title-career">CAREER</h1>
  <h1 class="title title-counseling">COUNSELING</h1>

  <div class="intro">
    <div class="intro-lead">Do you recognize yourself in</div>
    <div class="intro-sub">any of the following questions?</div>
  </div>

  <!-- questions left -->
  <div class="question" style="left:72px;top:474px">
    <svg width="40" height="40" viewBox="0 0 40 40"><circle cx="20" cy="20" r="18.5" fill="none" stroke="var(--slate)" stroke-width="1.6"/><path d="M24,8L13,22H19L16,32L27,17H21Z" fill="var(--teal)"/></svg>
    <p>How can I get<br>more energy from my job?</p>
  </div>
  <div class="question" style="left:72px;top:533px">
    <svg width="40" height="40" viewBox="0 0 40 40"><circle cx="20" cy="20" r="18.5" fill="none" stroke="var(--slate)" stroke-width="1.6"/><circle cx="20" cy="20" r="13" fill="var(--teal)"/><path d="M20,7A6.5,6.5 0 0 1 20,20A6.5,6.5 0 0 0 20,33A13,13 0 0 0 20,7Z" fill="var(--white)"/></svg>
    <p>How can I get<br>a better work-life balance?</p>
  </div>
  <div class="question" style="left:72px;top:589px">
    <svg width="40" height="40" viewBox="0 0 40 40"><circle cx="20" cy="20" r="18.5" fill="none" stroke="var(--slate)" stroke-width="1.6"/><circle cx="20" cy="19" r="4.5" fill="var(--slate)"/><path d="M11,31C11,25 15,24 20,24C25,24 29,25 29,31Z" fill="var(--slate)"/><g fill="var(--teal)"><circle cx="11" cy="14" r="1.6"/><circle cx="15" cy="10" r="1.6"/><circle cx="20" cy="8.5" r="1.6"/><circle cx="25" cy="10" r="1.6"/><circle cx="29" cy="14" r="1.6"/></g></svg>
    <p>What are my talents?</p>
  </div>

  <!-- questions right -->
  <div class="question" style="left:397px;top:479px">
    <svg width="40" height="40" viewBox="0 0 40 40"><circle cx="20" cy="20" r="18.5" fill="none" stroke="var(--slate)" stroke-width="1.6"/><path d="M7,17L13,14L20,16L27,14L33,17L28,24L22,27L16,25L11,22Z" fill="var(--slate)"/><path d="M14,19L20,18L26,22" stroke="var(--white)" stroke-width="1.5" fill="none"/></svg>
    <p>How can I work better with my manager<br>and/or colleagues?</p>
  </div>
  <div class="question" style="left:397px;top:539px">
    <svg width="40" height="40" viewBox="0 0 40 40"><circle cx="20" cy="20" r="18.5" fill="none" stroke="var(--slate)" stroke-width="1.6"/><path d="M20,8A8,8 0 0 0 15,22V26H25V22A8,8 0 0 0 20,8Z" fill="var(--teal)"/><rect x="16" y="28" width="8" height="2.5" rx="1" fill="var(--slate)"/><path d="M16.5,16L19,19L24,13" stroke="var(--white)" stroke-width="2" fill="none"/></svg>
    <p>Do you know what you want, but do not<br>dare to take the step?</p>
  </div>
  <div class="question" style="left:397px;top:600px">
    <svg width="40" height="40" viewBox="0 0 40 40"><circle cx="20" cy="20" r="18.5" fill="none" stroke="var(--slate)" stroke-width="1.6"/><rect x="10" y="18" width="5" height="12" rx="1" fill="var(--slate)"/><path d="M16,18L20,9C23,9 23,12 22,16H28C30,16 30,19 28,19C30,20 30,23 28,23C29,24 29,27 27,27C28,29 27,30 25,30H16Z" fill="var(--teal)"/></svg>
    <p>Or maybe you think you have more up<br>your sleeve than you do today?</p>
  </div>

  <div class="coach-glow"></div>
  <div class="coach-photo" role="img" aria-label="Photo of the coach in a burgundy shirt, standing and smiling"></div>

  <div class="story">
    <p class="w1"><svg class="tick" width="26" height="22" viewBox="0 0 26 22"><path d="M2,11L9,18L24,3" stroke="var(--teal)" stroke-width="4.5" fill="none" stroke-linecap="round" stroke-linejoin="round"/></svg>We easily spend 8 hours a day on our professional pursuits, our job. If we assume that we sleep about 8 hours a day, that's 50% of our active time. We actually spend more time with our colleagues than with our partner and/or children.</p>
    <p class="w1"><svg class="tick" width="26" height="22" viewBox="0 0 26 22"><path d="M2,11L9,18L24,3" stroke="var(--teal)" stroke-width="4.5" fill="none" stroke-linecap="round" stroke-linejoin="round"/></svg>In addition, if things are not going well during those 8 hours, it also impacts the other 8 working hours. If we don't feel good about ourselves at work, our family members, friends and acquaintances feel it too.</p>
    <p class="w1"><svg class="tick" width="26" height="22" viewBox="0 0 26 22"><path d="M2,11L9,18L24,3" stroke="var(--teal)" stroke-width="4.5" fill="none" stroke-linecap="round" stroke-linejoin="round"/></svg>So we'd better make sure that we spend those 8 hours meaningfully and, at best, get energy from it too. That we can accomplish a piece of our personal accomplishments there.</p>
    <p class="w4">Unfortunately, not every career goes smoothly, and it is even very normal that there are ups and downs this, nowadays more than 40-year career. But we can strive to keep these downs as short as possible and the ups as long as possible.</p>
    <p class="w5">And that's where Career Counseling comes into play.</p>
    <p class="w6">During this career counseling, we take a close look at your personal situation.</p>
  </div>

  <footer class="footer"></footer>
  <div class="ribbon">Career guidance cheques of the GBRO</div>

  <div class="contacts">
    <div class="contact">
      <svg width="28" height="18" viewBox="0 0 28 18"><rect x="1" y="1" width="26" height="16" fill="var(--teal)"/><path d="M1,1L14,11L27,1M1,17L11,8.5M27,17L17,8.5" stroke="var(--night)" stroke-width="1.6" fill="none"/></svg>
      <span>tom.verlinde@movalcoaching.example</span>
    </div>
    <div class="contact">
      <svg width="24" height="24" viewBox="0 0 24 24"><circle cx="12" cy="12" r="10.5" fill="none" stroke="var(--teal)" stroke-width="2"/><ellipse cx="12" cy="12" rx="4.5" ry="10.5" fill="none" stroke="var(--teal)" stroke-width="1.6"/><path d="M2,12H22M4,7H20M4,17H20" stroke="var(--teal)" stroke-width="1.4"/></svg>
      <span>www.movalcoaching.example</span>
    </div>
    <div class="contact contact-phone">
      <svg width="22" height="24" viewBox="0 0 22 24"><path d="M5,1L9,6L6.5,9C8,13 10,16 13.5,18L16.5,15.5L21,19.5L18,23C9,22 1,12 1,4Z" fill="var(--teal)"/></svg>
      <span>0472/318946</span>
    </div>
  </div>

</div>
</body>
</html>
```